Varrow Business Card Design - Professional Flexible and forward thinking. Clean and Easy to follow

Management Consulting Company. I focus on business development and concept and operational review. I need a progressive, simple and professional layout design for the business cards, letterhead and envelops
Professional Flexible and forward thinking. Clean and Easy to follow
Mature Business persons and professionals and Corporations

Target Market(s)

Mature Business persons and professionals and Corporations - Government org.

Industry/Entity Type

Consulting

Contact Information for Business Card

Requirements
Must have
• Marcus Varrow
• President
• Phone - 347.682.1530
• email - Mvarrow@varrowpartners-example.com
• Skype - Marc.varrow
• 2187 Tollbrook Lane
• Suite 4
• Harlow Bay, N.Y. 11492
• USA
Nice to have
• www.varrowpartners-example.com
Should not have
• N/A

```html
<!DOCTYPE html>
<html lang="en">
<head>
<meta charset="utf-8">
<title>Varrow Business Card Design</title>
<link href="https://fonts.googleapis.com/css2?family=Arvo:wght@700&family=Ubuntu:wght@400;500&display=swap" rel="stylesheet">
<style>
  :root {
    --backdrop: #e9eef1;
    --ink: #111111;
    --paper: #f5f6f8;
    --accent: #e8242b;
    --white: #ffffff;
  }
  * { box-sizing: border-box; margin: 0; padding: 0; }
  html, body {
    width: 1200px; height: 900px; overflow: hidden;
    background: var(--backdrop);
    font-family: "Ubuntu", Arial, sans-serif;
  }
  .sheet {
    position: relative; width: 1200px; height: 900px;
    display: flex; flex-direction: column; align-items: center; justify-content: center; gap: 50px;
  }
  .card {
    position: relative; width: 600px; height: 343px; overflow: hidden;
    box-shadow: 0 6px 22px rgba(0,0,0,0.12);
  }

  /* Front */
  .card--front { background: var(--ink); color: var(--white); }
  .front-mark {
    position: absolute; top: 108px; left: 0; width: 100%;
    text-align: center; font-weight: 500; font-size: 30px; letter-spacing: 2px;
  }
  .front-tagline {
    position: absolute; bottom: 42px; left: 0; width: 100%;
    text-align: center; font-size: 15px; letter-spacing: 0.3px;
  }
  .front-tagline .dot {
    display: inline-block; width: 7px; height: 7px; border-radius: 50%;
    background: var(--white); margin: 0 12px; vertical-align: middle;
  }

  /* Back */
  .card--back { background: var(--paper); color: var(--ink); }
  .back-mark {
    position: absolute; top: 30px; right: 68px;
    display: flex; align-items: center; gap: 10px;
    font-weight: 500; font-size: 20px;
  }
  .back-mark .square { width: 40px; height: 40px; background: var(--ink); }
  .back-bar { position: absolute; top: 30px; right: 0; width: 60px; height: 40px; background: var(--ink); }

  .accent-bar { position: absolute; left: 0; top: 148px; width: 22px; height: 50px; background: var(--accent); }
  .person { position: absolute; left: 40px; top: 140px; }
  .person-name { font-family: "Arvo", Georgia, serif; font-weight: 700; font-size: 30px; line-height: 1.05; }
  .person-title { font-size: 18px; margin-top: 3px; padding-left: 12px; }

  .contact { list-style: none; position: absolute; }
  .contact li { display: flex; align-items: center; gap: 9px; font-size: 15px; line-height: 25px; }
  .contact svg { width: 16px; height: 16px; flex: none; fill: var(--ink); }
  .contact--direct { left: 66px; top: 238px; }
  .contact--office { left: 352px; top: 122px; }
  .contact--office li { font-size: 13px; line-height: 19px; align-items: flex-start; }
  .contact--office svg { margin-top: 2px; }
  .address-lines { display: block; }
</style>
</head>
<body>
<main class="sheet">

  <section class="card card--front" aria-label="Card front">
    <div class="front-mark">Varrow</div>
    <p class="front-tagline">Business Development and Concept<span class="dot"></span>Operational Review</p>
  </section>

  <section class="card card--back" aria-label="Card back">
    <div class="back-mark"><span>Varrow</span><span class="square"></span></div>
    <div class="back-bar"></div>

    <div class="accent-bar"></div>
    <div class="person">
      <h1 class="person-name">Marcus Varrow</h1>
      <p class="person-title">President</p>
    </div>

    <ul class="contact contact--direct">
      <li>
        <svg viewBox="0 0 24 24" aria-hidden="true"><path d="M6.6 10.8a15.1 15.1 0 0 0 6.6 6.6l2.2-2.2a1 1 0 0 1 1-.25 11.4 11.4 0 0 0 3.6.57 1 1 0 0 1 1 1V20a1 1 0 0 1-1 1A17 17 0 0 1 3 4a1 1 0 0 1 1-1h3.5a1 1 0 0 1 1 1c0 1.25.2 2.45.57 3.6a1 1 0 0 1-.25 1z"/></svg>
        347 - 682 - 1530
      </li>
      <li>
        <svg viewBox="0 0 24 24" aria-hidden="true"><path d="M2 5h20v14H2z M4 7v.4l8 5.2 8-5.2V7z" fill-rule="evenodd"/></svg>
        Mvarrow@varrowpartners-example.com
      </li>
      <li>
        <svg viewBox="0 0 24 24" aria-hidden="true"><circle cx="12" cy="12" r="10"/></svg>
        Marc.varrow
      </li>
    </ul>

    <ul class="contact contact--office">
      <li>
        <svg viewBox="0 0 24 24" aria-hidden="true"><path d="M10.6 13.4a1 1 0 0 1 0-1.4l3.5-3.5a1 1 0 1 1 1.4 1.4L12 13.4a1 1 0 0 1-1.4 0zM8.5 11.3l-2.8 2.8a3.5 3.5 0 0 0 5 5l2.8-2.8-1.4-1.4-2.8 2.8a1.5 1.5 0 0 1-2.2-2.2l2.8-2.8zm7-1.4 2.8-2.8a3.5 3.5 0 0 0-5-5l-2.8 2.8 1.4 1.4 2.8-2.8a1.5 1.5 0 0 1 2.2 2.2l-2.8 2.8z"/></svg>
        www.varrowpartners-example.com
      </li>
      <li>
        <svg viewBox="0 0 24 24" aria-hidden="true"><path d="M12 2a7 7 0 0 0-7 7c0 5.2 7 13 7 13s7-7.8 7-13a7 7 0 0 0-7-7zm0 9.5A2.5 2.5 0 1 1 12 6.5a2.5 2.5 0 0 1 0 5z"/></svg>
        <span class="address-lines">2187 Tollbrook Lane<br>Suite 4<br>Harlow Bay, N.Y. 11492<br>USA</span>
      </li>
    </ul>
  </section>

</main>
</body>
</html>
```